依頼概要
■依頼の目的/概要
弊社が販売しているフルーツトマト(高糖度トマト)のパッケージのラベルデザインをお願いします。

■依頼詳細
弊社はトマトの栽培をしています。場所は長崎県壱岐市で玄界灘の島です。
ルナフィル栽培というフィルムで栽培する新しい栽培方法です。島内のスーパーで販売しており大変好評です。糖度が8度以上あり、小さな子供さんからお年寄りまで喜んで食べて頂いています。トマト嫌いの人もこのトマトなら食べれるといって食べる方もいらっしゃいます。予想以上の好評で今回栽培面積を増やし関東への販路を考えております。これまで「ぽかぽか丸」(子供が美味しくてパクパク食べてすぐ無くなり、また買ってと何回もせがまれママを泣かせる)というネーミングで販売していましたが。関東進出を期にネーミングを「そよ花」にバージョンアップして、新しいラベルの作成を企画しております。
<ラベルの仕様>
1.トマト1粒が20g~40gのミディートマトを150g~250gのパッケージで販売することを想定して、そのパッケージに貼るラベルです。
2.ラベルの大きさは、36×45角丸5R (mm)
3.ラベルに盛込む内容は添付ファイルの内容と同じで「ぽかぽか丸」を「そよ花」に変更(デザインにマッチする方を選択して下さい)

■その他要望
高品質が売りですから、高級感と「一目で食べてみたい」と思うようなラベルにして欲しい。
■ 選んだ理由

非常に洗練されたデザインが決めてです。
少し修正をお願いしたいのですが、よろしくお願いします。

■ 提案者全員のお礼・コメント

ご提案有難うございました。
これからもよろしくお願いします。

```html
<!DOCTYPE html>
<html lang="ja">
<head>
<meta charset="utf-8">
<title>フルーツトマト「そよ花」ラベルデザイン</title>
<link rel="stylesheet" href="https://fonts.googleapis.com/css2?family=Noto+Sans+JP:wght@400&family=Shippori+Mincho:wght@500;700&display=swap">
<style>
  :root {
    --paper: #ffffff;
    --ink: #333333;
    --mark: #222222;
    --brown: #5e4330;
    --tomato: #c8322a;
    --tomato-soft: #f3d2cc;
    --leaf: #6f9a4c;
    --leaf-dark: #3f6a2a;
  }
  * { margin: 0; padding: 0; box-sizing: border-box; }
  html, body { width: 848px; height: 1200px; overflow: hidden; background: var(--paper); }
  .sheet { position: relative; width: 848px; height: 1200px; }
  .proof-info {
    position: absolute; left: 84px; top: 78px;
    font-family: "Noto Sans JP", sans-serif; font-size: 21px; line-height: 48px; color: var(--ink);
  }
  .trim-marks { position: absolute; inset: 0; }
  .label {
    position: absolute; left: 184px; top: 395px; width: 494px; height: 392px;
    border: 3px solid #4a4a4a; border-radius: 34px; overflow: hidden; background: var(--paper);
  }
  .crest {
    position: absolute; left: 225px; top: 14px; width: 44px; height: 28px;
    background: radial-gradient(ellipse at 50% 80%, var(--tomato) 0 45%, transparent 70%);
  }
  .tagline {
    position: absolute; top: 42px; width: 100%; text-align: center;
    font-family: "Shippori Mincho", serif; font-weight: 500; font-size: 34px; line-height: 1.2; letter-spacing: 2px; color: var(--brown);
  }
  .product-name {
    position: absolute; top: 90px; width: 100%; text-align: center;
    font-family: "Shippori Mincho", serif; font-weight: 700; font-size: 90px; line-height: 1; letter-spacing: 14px; color: var(--brown);
  }
  .method-band {
    position: absolute; left: 90px; right: 0; top: 202px; height: 44px; background: var(--leaf);
    font-family: "Shippori Mincho", serif; font-weight: 500; font-size: 27px; letter-spacing: 5px;
    color: var(--paper); line-height: 44px; padding-left: 112px;
  }
  .pattern {
    position: absolute; left: 0; right: 0; top: 252px; bottom: 0;
    background: linear-gradient(180deg, var(--tomato-soft), #e59a8f 55%, var(--tomato-soft));
  }
  .origin-badge {
    position: absolute; left: 8px; top: 198px; width: 148px; height: 148px; border-radius: 50%;
    background: var(--paper); border: 5px solid var(--leaf);
    display: flex; flex-direction: column; align-items: center; justify-content: center;
    font-family: "Shippori Mincho", serif; font-weight: 700; font-size: 28px; line-height: 1.2; color: var(--leaf-dark);
  }
</style>
</head>
<body>
<div class="sheet">
  <div class="proof-info">
    <p>kanda 様</p>
    <p>フルーツトマト「そよ花」パッケージデザイン</p>
    <p>サイズ：36×45 角丸 5R (mm)</p>
  </div>

  <svg class="trim-marks" width="848" height="1200" viewBox="0 0 848 1200" fill="none" stroke="var(--mark)" stroke-width="1.5">
    <path d="M184 300 V380 M145 300 V380 M90 395 H170 M90 358 H170"/>
    <path d="M678 300 V380 M717 300 V380 M692 395 H772 M692 358 H772"/>
    <path d="M184 802 V890 M145 802 V890 M90 787 H170 M90 824 H170"/>
    <path d="M678 802 V890 M717 802 V890 M692 787 H772 M692 824 H772"/>
  </svg>

  <div class="label">
    <div class="crest" role="img" aria-label="小さな赤い花の飾り"></div>
    <p class="tagline">フルーツトマト</p>
    <h1 class="product-name">そよ花</h1>
    <div class="method-band">ルナフィル栽培</div>
    <div class="pattern" role="img" aria-label="赤い線で描かれたトマトと草花の装飾模様"></div>
    <div class="origin-badge"><span>長崎県</span><span>壱岐産</span></div>
  </div>
</div>
</body>
</html>
```